ORVILMA card Technical Architecture

Hello everyone ORVILMA: It is a consulting firm in Architecture and Construction. I require a card duplexing, sober, elegant, classic but not boring. Update 1: Use the following data for the card. Name: Rodrigo Salinas Tomás Quevedo Position: COO Twitter: @orvilmaAT Homepage: orvilma.com home address not include the participation of all thank you.

Target Market(s)

Construction companies, Architects and Consulting Engineers

Industry/Entity Type

Consulting

Contact Information for Business Card

Los campos que debe tener:
Nombre, Cargo, email, homepage y twitter

Font styles to use
Serif
Sans Serif
Other font styles liked:
• Me gustan playfair display, open sans y roboto, pero estoy sujeto a sus propuestas

Requirements
Must have
• Colors: Present combined proposals in white, red, gray and black Update 1: The two names must be clearly differentiated from the two surnames
Nice to have
• They are free to present their best proposals. I will bring them immediate feedback to the extent you can go see their designs. Complete data for card and logo files will give the winner the

```html
<!DOCTYPE html>
<html lang="es">
<head>
<meta charset="utf-8">
<title>ORVILMA – Tarjeta de presentación</title>
<link rel="stylesheet" href="https://fonts.googleapis.com/css2?family=Playfair+Display+SC:wght@400;700&family=Playfair+Display:wght@400&family=Montserrat:wght@300;400&display=swap">
<style>
  :root {
    --backdrop: #808087;
    --paper: #f3f2f0;
    --ink: #1c1c1c;
    --card-black: #0a0a0b;
    --brand-red: #a3161f;
    --brand-red-dark: #7d0f16;
    --white: #ffffff;
  }
  * { margin: 0; padding: 0; box-sizing: border-box; }
  html, body {
    width: 1200px; height: 900px; overflow: hidden;
    background: var(--backdrop);
  }
  .canvas {
    width: 1200px; height: 900px;
    display: flex; flex-direction: column;
    align-items: center; justify-content: center; gap: 48px;
  }
  .card {
    position: relative; width: 660px; height: 378px;
    overflow: hidden;
    box-shadow: 0 6px 18px rgba(0,0,0,0.25);
  }

  /* Front */
  .card--front { background: var(--paper); }
  .card__bands { position: absolute; inset: 0; width: 100%; height: 100%; }
  .front__content {
    position: absolute; left: 0; right: 0; top: 92px;
    text-align: center; color: var(--ink);
  }
  .front__brand {
    font-family: "Playfair Display", serif;
    font-size: 26px; letter-spacing: 6px;
    color: var(--brand-red);
    margin-bottom: 18px;
  }
  .front__name {
    font-family: "Playfair Display SC", serif;
    line-height: 1;
  }
  .front__given { font-size: 15px; letter-spacing: 0.5px; }
  .front__surname { font-size: 22px; letter-spacing: 0.5px; }
  .front__role {
    font-family: "Playfair Display SC", serif;
    font-size: 12px; color: var(--brand-red);
    letter-spacing: 0.6px; margin-top: 6px;
  }
  .front__phone {
    font-family: "Playfair Display", serif;
    font-size: 21px; margin-top: 10px;
  }

  /* Back */
  .card--back { background: var(--card-black); color: var(--white); }
  .back__lockup {
    position: absolute; left: 90px; width: 360px; top: 112px;
    text-align: center;
  }
  .back__brand {
    font-family: "Montserrat", sans-serif; font-weight: 300;
    font-size: 40px; line-height: 1.2;
    letter-spacing: 12px; padding-left: 12px;
    color: var(--white);
  }
  .back__rule {
    width: 280px; height: 1px; margin: 8px auto 7px;
    background: var(--brand-red);
  }
  .back__tagline {
    font-family: "Montserrat", sans-serif; font-weight: 400;
    font-size: 12px; letter-spacing: 4px; padding-left: 4px;
    color: var(--brand-red);
  }
  .back__contact {
    position: absolute;
    font-family: "Playfair Display SC", serif;
    font-size: 15px; letter-spacing: 0.4px;
    white-space: nowrap;
  }
  .back__contact--twitter { right: 36px; top: 222px; }
  .back__contact--web { left: 36px; bottom: 30px; }
</style>
</head>
<body>
<main class="canvas">

  <section class="card card--front" aria-label="Tarjeta, cara frontal">
    <svg class="card__bands" viewBox="0 0 660 378" aria-hidden="true">
      <path fill="var(--brand-red)" d="M92 0 H110 C118 140 140 260 180 378 H160 C118 260 96 140 92 0 Z"/>
      <path fill="var(--brand-red)" d="M126 0 H196 C194 130 210 260 250 378 H196 C150 260 128 130 126 0 Z"/>
      <path fill="var(--brand-red-dark)" d="M470 0 H528 C520 130 560 260 620 378 H566 C504 260 470 130 470 0 Z"/>
      <path fill="var(--brand-red-dark)" d="M540 0 H556 C552 130 596 260 660 360 V378 H648 C584 260 540 130 540 0 Z"/>
    </svg>
    <div class="front__content">
      <p class="front__brand">ORVILMA</p>
      <p class="front__name">
        <span class="front__given">Rodrigo Salinas</span>
        <span class="front__surname">Tomás Quevedo</span>
      </p>
      <p class="front__role">Director de Operaciones</p>
      <p class="front__phone">(+571) 555 010 2040</p>
    </div>
  </section>

  <section class="card card--back" aria-label="Tarjeta, cara posterior">
    <div class="back__lockup">
      <p class="back__brand">ORVILMA</p>
      <div class="back__rule"></div>
      <p class="back__tagline">ARQUITECTURA TÉCNICA</p>
    </div>
    <p class="back__contact back__contact--twitter">Twitter: @orvilmaAT</p>
    <p class="back__contact back__contact--web">Webpage: orvilma.com</p>
  </section>

</main>
</body>
</html>
```